Carton Box Packaging For Motorcycle Brake Shoe - Varonel Brand

Packaging Dimensions: 125mm (H) x 125mm (W) x 31mm (D)
We would like to design a genuine Carton box Packaging for motorcycle Brake Shoe.
This is a critical part of the motorcycle, so we need the packaging to reflect elegant impression.
Varonel, is one of the leading companies for manufacturing Motorcycles, located in Egypt. Our company is offering high-quality products, the best in the local market, with very competitive prices.
We have a limited time to get this project done, So we Highly appreciate receiving your designs ASAP.
Target Market(s)
Economical Motorcycle Buyers
Colors
Designer to choose colors to be used in the design.
Look and feel

```html
<!DOCTYPE html>
<html lang="en">
<head>
<meta charset="utf-8">
<title>Varonel Motorcycle Brake Shoe – Carton Lid</title>
<link rel="stylesheet" href="https://fonts.googleapis.com/css2?family=EB+Garamond:wght@400;500;600&display=swap">
<style>
  :root {
    --backdrop: #f2f2f2;
    --carton-white: #ffffff;
    --brand-red: #cc242b;
    --ink-black: #0b0b0b;
    --steel-dark: #7d7d7d;
    --steel-mid: #bdbdbd;
    --steel-light: #f4f4f4;
    --photo-dark: #4a4a4a;
    --photo-light: #d6d6d6;
  }
  html, body {
    margin: 0;
    width: 1200px;
    height: 1072px;
    overflow: hidden;
    background: var(--backdrop);
  }
  .carton-lid {
    position: absolute;
    left: 150px;
    top: 86px;
    width: 900px;
    height: 900px;
    box-shadow: 0 10px 40px rgba(0,0,0,0.12);
    background: var(--carton-white);
  }
  .carton-lid svg { display: block; }
  .lid-title {
    font-family: "EB Garamond", Georgia, serif;
    font-weight: 500;
    font-size: 66px;
    fill: var(--ink-black);
  }
  .brand-name {
    font-family: "EB Garamond", Georgia, serif;
    font-weight: 500;
    font-size: 34px;
    fill: var(--ink-black);
  }
  .product-copy {
    font-family: "EB Garamond", Georgia, serif;
    font-weight: 400;
    font-size: 16px;
    fill: var(--carton-white);
  }
</style>
</head>
<body>
  <div class="carton-lid">
    <svg width="900" height="900" viewBox="0 0 900 900" xmlns="http://www.w3.org/2000/svg">
      <defs>
        <linearGradient id="brushed-steel" x1="0" y1="0" x2="1" y2="0.4">
          <stop offset="0" stop-color="var(--steel-dark)"/>
          <stop offset="0.3" stop-color="var(--steel-mid)"/>
          <stop offset="0.5" stop-color="var(--steel-light)"/>
          <stop offset="0.75" stop-color="var(--steel-mid)"/>
          <stop offset="1" stop-color="var(--steel-dark)"/>
        </linearGradient>
        <pattern id="brush-lines" width="900" height="3" patternUnits="userSpaceOnUse">
          <rect width="900" height="1" fill="rgba(255,255,255,0.12)"/>
        </pattern>
        <linearGradient id="shoe-photo-tone" x1="0" y1="0" x2="1" y2="1">
          <stop offset="0" stop-color="var(--photo-light)"/>
          <stop offset="0.6" stop-color="var(--photo-dark)"/>
          <stop offset="1" stop-color="var(--photo-light)"/>
        </linearGradient>
      </defs>

      <!-- large letter A -->
      <polygon class="a-shadow-left" points="140,0 185,0 0,600 0,540" fill="var(--ink-black)"/>
      <polygon class="a-leg-left" points="185,0 340,0 0,780 0,600" fill="var(--brand-red)"/>
      <polygon class="a-leg-right" points="185,0 522,0 860,900 545,900" fill="var(--brand-red)"/>
      <polygon class="a-shadow-right" points="522,0 572,0 900,690 900,900 860,900" fill="var(--ink-black)"/>

      <!-- copy strip -->
      <rect class="copy-strip" x="40" y="423" width="430" height="190" fill="var(--ink-black)"/>

      <!-- steel band -->
      <rect class="steel-band" x="0" y="207" width="900" height="216" fill="url(#brushed-steel)"/>
      <rect x="0" y="207" width="900" height="216" fill="url(#brush-lines)"/>

      <text class="lid-title" x="60" y="292">Varonel</text>
      <text class="lid-title" x="60" y="376">Motorcycle Brake Shoe</text>

      <g class="brand-mark">
        <circle cx="690" cy="255" r="14" fill="var(--ink-black)"/>
        <text class="brand-name" x="714" y="267">Varonel</text>
      </g>

      <!-- product copy -->
      <text class="product-copy" x="60" y="460">Varonel Motorcycle Brake Shoe is the high quality and perfect fit.</text>
      <text class="product-copy" x="60" y="484">Varonel Motorcycle Brake Shoe is intended to be a direct replacement</text>
      <text class="product-copy" x="60" y="508">for O.E.M. pads and shoe and meet O.E.M. performance.</text>
      <text class="product-copy" x="60" y="532">Varonel Motorcycle Brake Shoe is formulated for high-performance</text>
      <text class="product-copy" x="60" y="556">stopping power and a long service life.</text>

      <!-- product photograph area -->
      <rect class="shoe-photo" role="img" aria-label="Photograph of a motorcycle drum brake shoe pair with spring"
            x="30" y="650" width="430" height="250" fill="url(#shoe-photo-tone)"/>

      <!-- speed stripes -->
      <g class="speed-stripes">
        <rect x="780" y="690" width="80" height="7" fill="var(--ink-black)"/>
        <rect x="780" y="704" width="80" height="7" fill="var(--carton-white)"/>
        <rect x="780" y="718" width="80" height="7" fill="var(--ink-black)"/>
        <rect x="780" y="732" width="80" height="7" fill="var(--carton-white)"/>
      </g>
    </svg>
  </div>
</body>
</html>
```